Anzeigengestaltung für Steuerberaterin
Zielgruppe
Ich bin Steuerberaterin und Zertizierter Testamentsvollstrecker (BKW) in Gerlingen.
Wir sind keine kleine, innovative Steuerkanzlei und möchten vor allem Mandanten ansprechen, den eine digitale Zusammenarbeit wichtig ist.
Zielgruppe: Startups, kleine Unternehmen oder Freiberufler, Gemeinnützige Organisationen
Software: Datev, Buchhaltungsbutler, sevDesk
Aufgabenstellung
Nach meinem Umzug in größere Büroräume benötige ich eine Anzeige im Format 90 x 80 mm für eine Zeitung.
Auf der Anzeige sollte ein Umzugshinweis enthalten sein. Die Anzeige würde ich gerne wieder verwenden. (eine version ohne Umzugshinweis)
Slogan: Gemeinsam Steuern Gestalten

```html
<!DOCTYPE html>
<html lang="de">
<head>
<meta charset="utf-8">
<title>Anzeige Steuerkanzlei Lotte Krause</title>
<link rel="stylesheet" href="https://fonts.googleapis.com/css2?family=Arimo:wght@400;700&family=Didact+Gothic&display=swap">
<style>
  :root{
    --page:#d9d9d9;
    --navy:#1c4c9e;
    --cyan:#1fb3ec;
    --grey:#9a9a9a;
    --slogan:#9b9b9b;
    --ink:#2a4f94;
    --white:#ffffff;
  }
  *{margin:0;padding:0;box-sizing:border-box}
  html,body{width:1200px;height:676px;overflow:hidden;background:var(--page)}
  .stage{position:relative;width:1200px;height:676px}
  .ad{
    position:absolute;top:106px;width:576px;height:513px;
    background:var(--white);border:1px solid var(--navy);overflow:hidden;
    font-family:"Arimo",Arial,sans-serif;
  }
  .ad--move{left:14px}
  .ad--plain{left:614px}
  .ad__photo{
    position:absolute;left:0;top:0;width:100%;height:300px;
    background:
      linear-gradient(to bottom,rgba(255,255,255,0) 45%,#fff 100%),
      linear-gradient(100deg,#c9b7a8 0%,#e3b7b5 25%,#b9d0d4 50%,#e8eef0 70%,#9fb8bf 100%);
  }
  .ad__ribbon{
    position:absolute;left:352px;top:26px;width:222px;height:36px;
    background:var(--cyan);color:var(--white);
    transform:rotate(-8deg);transform-origin:left center;
    font-family:"Didact Gothic",sans-serif;font-size:23px;line-height:36px;padding-left:9px;
  }
  .ad__headline{
    position:absolute;left:15px;top:198px;width:540px;
    color:var(--navy);font-weight:700;font-size:30px;line-height:31px;
  }
  .ad__focus{position:absolute;left:16px;top:303px;color:var(--ink);font-size:15.5px}
  .ad__focus-title{text-decoration:underline;margin-bottom:9px}
  .ad__item{display:flex;align-items:center;gap:8px;height:27px;margin-left:-3px}
  .ad__item svg{width:20px;height:20px;flex:none}
  .ad__bands{position:absolute;left:0;top:385px;width:576px;height:60px}
  .ad__slogan{
    position:absolute;left:18px;top:470px;color:var(--slogan);
    font-family:"Didact Gothic",sans-serif;font-size:27px;line-height:30px;
  }
  .ad__portrait{
    position:absolute;left:373px;top:428px;width:78px;height:78px;border-radius:50%;
    border:2px solid var(--navy);
    background:radial-gradient(circle at 50% 45%,#e3b39c 0%,#a8452f 60%,#6e1f1a 100%);
  }
  .ad__brand{
    position:absolute;left:468px;top:448px;width:104px;
    display:flex;flex-direction:column;align-items:center;gap:5px;
    color:var(--navy);font-weight:700;font-size:10px;letter-spacing:1px;text-align:center;line-height:11px;
  }
  .ad__brand-mark{width:22px;height:22px;background:var(--navy)}
</style>
</head>
<body>
<div class="stage">

  <section class="ad ad--move">
    <div class="ad__photo" role="img" aria-label="Foto: Frau im Büro zeigt mit Stift auf einen Bildschirm, darüber ein feines Netzwerkmuster"></div>
    <div class="ad__ribbon">Wir sind umgezogen!</div>
    <h1 class="ad__headline">Ihre Digitalkanzlei in Gerlingen für Startups, Unternehmen und Privatpersonen.</h1>
    <div class="ad__focus">
      <p class="ad__focus-title">Schwerpunkte:</p>
      <p class="ad__item"><svg viewBox="0 0 20 20"><circle cx="10" cy="10" r="8.5" fill="none" stroke="#2a4f94" stroke-width="1.4"/><path d="M5 10l4 4 9-12" fill="none" stroke="#2a4f94" stroke-width="1.8"/></svg>Erbschaftsteuer/Schenkungsteuer</p>
      <p class="ad__item"><svg viewBox="0 0 20 20"><circle cx="10" cy="10" r="8.5" fill="none" stroke="#2a4f94" stroke-width="1.4"/><path d="M5 10l4 4 9-12" fill="none" stroke="#2a4f94" stroke-width="1.8"/></svg>Testamentsgestaltung undTestamenstvollstreckung</p>
      <p class="ad__item"><svg viewBox="0 0 20 20"><circle cx="10" cy="10" r="8.5" fill="none" stroke="#2a4f94" stroke-width="1.4"/><path d="M5 10l4 4 9-12" fill="none" stroke="#2a4f94" stroke-width="1.8"/></svg>Gemeinnützigkeit</p>
    </div>
    <svg class="ad__bands" viewBox="0 0 576 60" preserveAspectRatio="none">
      <polygon points="25,56 576,6 576,24" fill="var(--grey)"/>
      <polygon points="0,33 576,0 576,6 0,52" fill="var(--navy)"/>
    </svg>
    <p class="ad__slogan">Gemeinsam Steuern Gestalten</p>
    <div class="ad__portrait" role="img" aria-label="Porträtfoto der Steuerberaterin"></div>
    <div class="ad__brand"><span class="ad__brand-mark"></span><span>STEUERKANZLEI<br>LOTTE KRAUSE</span></div>
  </section>

  <section class="ad ad--plain">
    <div class="ad__photo" role="img" aria-label="Foto: Frau im Büro zeigt mit Stift auf einen Bildschirm, darüber ein feines Netzwerkmuster"></div>
    <h1 class="ad__headline">Ihre Digitalkanzlei in Gerlingen für Startups, Unternehmen und Privatpersonen.</h1>
    <div class="ad__focus">
      <p class="ad__focus-title">Schwerpunkte:</p>
      <p class="ad__item"><svg viewBox="0 0 20 20"><circle cx="10" cy="10" r="8.5" fill="none" stroke="#2a4f94" stroke-width="1.4"/><path d="M5 10l4 4 9-12" fill="none" stroke="#2a4f94" stroke-width="1.8"/></svg>Erbschaftsteuer/Schenkungsteuer</p>
      <p class="ad__item"><svg viewBox="0 0 20 20"><circle cx="10" cy="10" r="8.5" fill="none" stroke="#2a4f94" stroke-width="1.4"/><path d="M5 10l4 4 9-12" fill="none" stroke="#2a4f94" stroke-width="1.8"/></svg>Testamentsgestaltung undTestamenstvollstreckung</p>
      <p class="ad__item"><svg viewBox="0 0 20 20"><circle cx="10" cy="10" r="8.5" fill="none" stroke="#2a4f94" stroke-width="1.4"/><path d="M5 10l4 4 9-12" fill="none" stroke="#2a4f94" stroke-width="1.8"/></svg>Gemeinnützigkeit</p>
    </div>
    <svg class="ad__bands" viewBox="0 0 576 60" preserveAspectRatio="none">
      <polygon points="25,56 576,6 576,24" fill="var(--grey)"/>
      <polygon points="0,33 576,0 576,6 0,52" fill="var(--navy)"/>
    </svg>
    <p class="ad__slogan">Gemeinsam Steuern Gestalten</p>
    <div class="ad__portrait" role="img" aria-label="Porträtfoto der Steuerberaterin"></div>
    <div class="ad__brand"><span class="ad__brand-mark"></span><span>STEUERKANZLEI<br>LOTTE KRAUSE</span></div>
  </section>

</div>
</body>
</html>
```